Business Cards Design for the electrical wholesaler: clean bold dynamic :)

We need a business card design that would follow our latest brand guidelines. As an electrical wholesaler we want to bring a fresh look and feel into the industry. The design should be clean bold and dynamic. It should come alive with the renewed energy of our green colour. Our grey colour should keep things balanced and complement the notion of maturity and responsibility. We employ Lato as a corporate font however are not bound by this font and we’re open to interpretation here.

Target Market(s)

Electrical contractors

Industry/Entity Type

Business

Contact Information for Business Card

Logo
Name & Surname: Olena Dovbush
Job Title: Director of Marketing
Email: helen.dovbush@mailvane.example
Cell phone: XXX.XXX.XXXX
Address: 20917 - 87 Ave. Edmonton, AB, Canada. T6K 2R8
Business Phone: 780.555.0187
Website: www.qorvil.example

Font styles to use
Other font styles liked:
• Lato

Requirements
Must have
• Logo & website
Nice to have
• Brand elements - some of them you may find in the attached Brand Guidelines (e.g. three lines on the background signifying "W")

```html
<!DOCTYPE html>
<html lang="en">
<head>
<meta charset="utf-8">
<title>Qorvil Business Card</title>
<link rel="stylesheet" href="https://fonts.googleapis.com/css2?family=Lato:wght@300;400;700;900&display=swap">
<style>
  :root {
    --green: #7ab733;
    --grey-dark: #4a4b4d;
    --grey-deep: #3f4042;
    --grey-text: #4d4e50;
    --rule: #9a9a9a;
    --paper: #ffffff;
    --paper-shade: #eeeeee;
    --backdrop: #a3a3a3;
  }
  * { margin: 0; padding: 0; box-sizing: border-box; }
  html, body { width: 1200px; height: 900px; overflow: hidden; }
  body {
    background: var(--backdrop);
    font-family: "Lato", Arial, sans-serif;
    position: relative;
  }
  .card {
    position: absolute;
    left: 250px;
    width: 700px;
    height: 400px;
    border-radius: 18px;
    overflow: hidden;
  }

  /* Back side */
  .card-back {
    top: 35px;
    background: linear-gradient(160deg, #505153 0%, var(--grey-dark) 55%, var(--grey-deep) 100%);
  }
  .card-back .backdrop-tone {
    position: absolute;
    inset: 0;
    background: radial-gradient(ellipse at 75% 25%, rgba(255,255,255,0.06), rgba(255,255,255,0) 60%);
  }
  .brand {
    position: absolute;
    display: flex;
    align-items: center;
    gap: 14px;
    font-weight: 400;
    letter-spacing: -1px;
    line-height: 1;
  }
  .brand-mark {
    display: block;
    background: var(--green);
  }
  .card-back .brand { left: 70px; top: 215px; font-size: 62px; color: #ffffff; }
  .card-back .brand-mark { width: 40px; height: 40px; }
  .card-back .website {
    position: absolute;
    left: 112px;
    top: 305px;
    font-size: 16px;
    letter-spacing: 3px;
    color: #ffffff;
  }
  .card-back .website .accent { color: var(--green); }

  /* Front side */
  .card-front {
    top: 465px;
    background: linear-gradient(180deg, var(--paper) 0%, var(--paper-shade) 100%);
  }
  .card-front .brand { left: 45px; top: 70px; font-size: 78px; color: var(--grey-text); }
  .card-front .brand-mark { width: 46px; height: 46px; }
  .identity {
    position: absolute;
    right: 40px;
    top: 170px;
    text-align: right;
  }
  .identity .person {
    font-size: 32px;
    font-weight: 900;
    color: var(--green);
    line-height: 1;
  }
  .identity .role {
    font-size: 18px;
    color: var(--grey-text);
    margin-top: 2px;
  }
  .divider {
    position: absolute;
    left: 40px;
    right: 40px;
    top: 232px;
    height: 1.5px;
    background: var(--rule);
  }
  .address {
    position: absolute;
    right: 40px;
    top: 248px;
    text-align: right;
    font-size: 18px;
    line-height: 1.35;
    color: var(--grey-text);
  }
  .contacts {
    position: absolute;
    left: 42px;
    top: 250px;
    list-style: none;
    font-size: 19px;
    color: var(--grey-text);
    line-height: 1;
  }
  .contacts li {
    display: flex;
    align-items: center;
    gap: 12px;
    height: 28px;
  }
  .contacts svg { width: 18px; height: 18px; flex: none; }
  .bottom-band {
    position: absolute;
    left: 0; bottom: 0;
    width: 700px; height: 400px;
  }
  .card-front .website {
    position: absolute;
    right: 40px;
    bottom: 28px;
    font-size: 17px;
    letter-spacing: 2.5px;
    color: #ffffff;
    white-space: nowrap;
  }
</style>
</head>
<body>

<section class="card card-back" aria-label="Card back">
  <div class="backdrop-tone"></div>
  <div class="brand"><span class="brand-mark"></span>qorvil</div>
  <p class="website">www.<span class="accent">qorvil</span>.example</p>
</section>

<section class="card card-front" aria-label="Card front">
  <svg class="bottom-band" viewBox="0 0 700 400" aria-hidden="true">
    <path d="M0 372 H396 C412 372 420 360 428 344" fill="none" stroke="var(--green)" stroke-width="6"/>
    <path d="M0 386 H410 C435 386 436 330 470 330 H700 V400 H0 Z" fill="var(--grey-dark)"/>
  </svg>

  <div class="brand"><span class="brand-mark"></span>qorvil</div>

  <div class="identity">
    <p class="person">Olena Dovbush</p>
    <p class="role">Director of Marketing</p>
  </div>

  <div class="divider"></div>

  <p class="address">20917 - 87 Ave. Edmonton<br>AB, Canada. T6K 2R8</p>

  <ul class="contacts">
    <li>
      <svg viewBox="0 0 18 18" aria-hidden="true"><rect x="4.5" y="1" width="9" height="16" rx="1.5" fill="none" stroke="var(--green)" stroke-width="1.8"/><rect x="7.5" y="13.5" width="3" height="1.5" fill="var(--green)"/></svg>
      780.555.0187
    </li>
    <li>
      <svg viewBox="0 0 18 18" aria-hidden="true"><path d="M4 2 L7 5 L5.5 7 C6.5 9.5 8.5 11.5 11 12.5 L13 11 L16 14 L14 16 C8 16 2 10 2 4 Z" fill="var(--green)"/></svg>
      780.555.0187
    </li>
    <li>
      <svg viewBox="0 0 18 18" aria-hidden="true"><rect x="1" y="4" width="16" height="11" fill="var(--green)"/><path d="M1 4 L9 10.5 L17 4" fill="none" stroke="#ffffff" stroke-width="1.4"/></svg>
      helen.dovbush@mailvane.example
    </li>
  </ul>

  <p class="website">www.qorvil.example</p>
</section>

</body>
</html>
```